Business Card for Bright Meadow Lawn & Landscape

Double Sided Card Design - I think one side of the card should be cleaner, with logo, contact info, and "Complete Residential & Commercial Landscape Services", and on the other side it should list the services we offer:

- Lawn Care & Mowing
- Hedge & Shrub Trimming
- Leaf Removal & Clean Up
- Aeration & Sod
- Mulch & Rock Installations
- Landscape Installations & Renovations
- Commercial Snow Removal

Please make it clean and very professional... don't want it too be too busy, but want to tell them what we do.

Target Market(s)

Residential and Commercial

Industry/Entity Type

Landscape

Contact Information for Business Card

Fully Insured
Tom Berrigan
410-555-0198
Tberrigan07@mailbox-example.com

Requirements
Must have
• Double Sided, Cleaner on one side, more information and text on the other side.

```html
<!DOCTYPE html>
<html lang="en">
<head>
<meta charset="utf-8">
<title>Bright Meadow Lawn &amp; Landscape – Business Card</title>
<link href="https://fonts.googleapis.com/css2?family=Roboto:wght@400;500;700&family=Roboto+Condensed:wght@700&display=swap" rel="stylesheet">
<style>
  :root {
    --backdrop: #6e4c36;
    --meadow-green: #8ab500;
    --card-black: #0b0b0b;
    --paper-white: #ffffff;
    --shadow: rgba(0, 0, 0, 0.45);
  }
  * { margin: 0; padding: 0; box-sizing: border-box; }
  html, body {
    width: 1200px;
    height: 960px;
    overflow: hidden;
  }
  body {
    position: relative;
    background: var(--backdrop);
    font-family: "Roboto", Arial, sans-serif;
    color: var(--paper-white);
  }
  .card {
    position: absolute;
    left: 320px;
    width: 600px;
    height: 342px;
    box-shadow: 0 4px 12px var(--shadow);
  }

  /* Services side */
  .card--services {
    top: 105px;
    background: var(--meadow-green);
  }
  .brand-mark {
    position: absolute;
    left: 0;
    right: 0;
    top: 112px;
    display: flex;
    align-items: center;
    justify-content: center;
    gap: 16px;
  }
  .brand-mark__dot {
    width: 52px;
    height: 52px;
    border-radius: 50%;
    background: var(--paper-white);
  }
  .brand-mark__name {
    font-size: 38px;
    font-weight: 500;
    letter-spacing: 0.5px;
    color: var(--paper-white);
  }
  .service-list {
    position: absolute;
    left: 0;
    right: 0;
    top: 252px;
    text-align: center;
    font-size: 14.5px;
    line-height: 19px;
    list-style: none;
  }

  /* Contact side */
  .card--contact {
    top: 493px;
    background: var(--card-black);
  }
  .contact-brand {
    position: absolute;
    right: 32px;
    top: 24px;
    display: flex;
    flex-direction: column;
    align-items: flex-end;
    gap: 12px;
  }
  .contact-brand__dot {
    width: 62px;
    height: 62px;
    border-radius: 50%;
    background: var(--meadow-green);
    margin-right: 46px;
  }
  .contact-brand__name {
    text-align: right;
    font-size: 18px;
    line-height: 21px;
    font-weight: 500;
    letter-spacing: 1.5px;
    text-transform: uppercase;
    color: var(--meadow-green);
  }
  .contact-details {
    position: absolute;
    left: 33px;
    top: 178px;
  }
  .contact-details__insured {
    font-family: "Roboto Condensed", "Arial Narrow", sans-serif;
    font-weight: 700;
    font-size: 22px;
    line-height: 26px;
    color: var(--meadow-green);
  }
  .contact-details__person {
    font-size: 18px;
    font-weight: 500;
    line-height: 24px;
    letter-spacing: 0.3px;
  }
  .contact-lines {
    list-style: none;
    margin-top: 14px;
    font-size: 14.5px;
    line-height: 20px;
  }
  .contact-lines li {
    display: flex;
    align-items: center;
    gap: 8px;
  }
  .contact-lines svg { fill: var(--meadow-green); }
  .contact-rule {
    position: absolute;
    left: 0;
    right: 0;
    top: 291px;
    height: 1px;
    background: var(--meadow-green);
  }
  .tagline {
    position: absolute;
    left: 30px;
    top: 299px;
    font-size: 16px;
    line-height: 20px;
  }
</style>
</head>
<body>

  <section class="card card--services" aria-label="Services side">
    <div class="brand-mark">
      <span class="brand-mark__dot"></span>
      <span class="brand-mark__name">Bright Meadow</span>
    </div>
    <ul class="service-list">
      <li>Lawn Care &amp; Mowing • Hedge &amp; Shrub Trimming</li>
      <li>Leaf Removal &amp; Clean Up • Aeration &amp; Sod • Mulch &amp; Rock Installations</li>
      <li>Landscape Installations &amp; Renovations • Commercial Snow Removal</li>
    </ul>
  </section>

  <section class="card card--contact" aria-label="Contact side">
    <div class="contact-brand">
      <span class="contact-brand__dot"></span>
      <p class="contact-brand__name">Bright Meadow<br>Lawn &amp; Landscape</p>
    </div>

    <div class="contact-details">
      <p class="contact-details__insured">FULLY INSURED</p>
      <p class="contact-details__person">TOM BERRIGAN</p>
      <ul class="contact-lines">
        <li>
          <svg width="12" height="14" viewBox="0 0 12 14" aria-hidden="true">
            <rect x="2" y="0" width="8" height="14" rx="1.5"/>
            <rect x="3.5" y="2" width="5" height="8" fill="#0b0b0b"/>
          </svg>
          410-555-0198
        </li>
        <li>
          <svg width="12" height="14" viewBox="0 0 12 14" aria-hidden="true">
            <rect x="0" y="3" width="12" height="8"/>
            <path d="M0 3 L6 8 L12 3" fill="none" stroke="#0b0b0b" stroke-width="1.2"/>
          </svg>
          Tberrigan07@mailbox-example.com
        </li>
      </ul>
    </div>

    <div class="contact-rule"></div>
    <p class="tagline">Complete Residential &amp; Commercial Landscape Services</p>
  </section>

</body>
</html>
```